Postcard Campaign Targeting School District Transportation Leaders

Design a campaign a 5 x 7 postcard.
Target: The postcard will be mailed to school district superintendents and their transportation leaders.
Messaging: That we offer an affordable software solution school transportation.
I am coming to their area and would like to stop by their office and introduce myself. (IF YOU PUT THIS LANGUAGE INTO YOUR SUBMISSION VERBATIM WITHOUT UNDERSTANDING THE MEANING YOUR SUBMISSION WILL BE REJECTED)
Goal: School district superintendents and their transportation leaders to know who we are and what we offer.   (IF YOU PUT THIS LANGUAGE INTO YOUR SUBMISSION VERBATIM WITHOUT UNDERSTANDING THE MEANING YOUR SUBMISSION WILL BE REJECTED)
Format: Please provide high resolution png or jpg file
Who We Are: VarnoTrak provides a solution for school transportation that integrates all features into a single, cloud based technology.
Features include:
Tracking Who, When and Where your buses were boarded and alighted
Live cloud reporting to find lost students

Load factor reporting to monitor efficiency.
Turn-by-turn directions to keep drivers updated and informed
Route Optimization saving more than 10% on transportation cost
Field Trip workflow to automate the athletic and field trips
Parent App to share bus information with your school community
Complete GPS Support
Our solutions have been designed working at the direction of our school district clients.
Here are examples of our social media content directed toward school districts.
https://www.brevalink.example/feed/update/urn:li:activity:4812093375610422871
https://www.brevalink.example/feed/update/urn:li:activity:4810287734196053310
https://www.brevalink.example/feed/update/urn:li:activity:4810273958241607725
https://www.brevalink.example/feed/update/urn:li:activity:4810269146738502934
https://www.brevalink.example/feed/update/urn:li:activity:4810258071369124857
https://www.brevalink.example/feed/update/urn:li:activity:4810241680935712043
https://www.brevalink.example/feed/update/urn:li:activity:4810236527148809361
https://www.brevalink.example/feed/update/urn:li:activity:4810225394601758412
https://www.brevalink.example/feed/update/urn:li:activity:4810217846027931596
https://www.brevalink.example/feed/update/urn:li:activity:4809172560938417285
https://www.brevalink.example/feed/update/urn:li:activity:4809148309751263017
https://www.brevalink.example/feed/update/urn:li:activity:4809103975264830148

```html
<!DOCTYPE html>
<html lang="en">
<head>
<meta charset="utf-8">
<title>VarnoTrak School Transportation Postcard</title>
<link href="https://fonts.googleapis.com/css2?family=Bebas+Neue&family=Lato:ital,wght@0,400;0,700;1,400&family=Montserrat:wght@300;400;700;800;900&display=swap" rel="stylesheet">
<style>
  :root {
    --page: #b3b3b3;
    --blue: #0b6cb8;
    --blue-deep: #0a4f8f;
    --green: #8ab22f;
    --white: #ffffff;
    --ink: #222a30;
    --ink-soft: #2c4757;
    --rule: #bfbfbf;
    --stamp: #f2f2f2;
  }
  * { box-sizing: border-box; margin: 0; padding: 0; }
  html, body { width: 1200px; height: 1200px; overflow: hidden; }
  body { background: var(--page); position: relative; font-family: "Lato", sans-serif; }

  .postcard {
    position: absolute;
    left: 255px;
    width: 699px;
    height: 499px;
    background: var(--white);
    overflow: hidden;
  }
  .postcard--front { top: 61px; }
  .postcard--back { top: 624px; }
  .postcard__art { position: absolute; inset: 0; }

  .brand { position: absolute; display: flex; align-items: center; gap: 10px; }
  .brand__dot { border-radius: 50%; background: var(--green); flex: none; }
  .brand__name { font-family: "Montserrat", sans-serif; font-weight: 700; color: var(--blue); letter-spacing: -0.5px; white-space: nowrap; }

  .front__brand { left: 43px; top: 414px; }
  .front__brand .brand__dot { width: 50px; height: 50px; }
  .front__brand .brand__name { font-size: 27px; }
  .front__divider { position: absolute; left: 267px; top: 416px; width: 1.5px; height: 58px; background: var(--ink); }
  .front__visit { position: absolute; left: 297px; top: 417px; width: 372px; font-size: 13px; line-height: 16px; color: var(--ink); }

  .tab {
    position: absolute; left: 0; width: 169px; height: 28px;
    border-radius: 0 14px 14px 0;
    font-family: "Montserrat", sans-serif; font-weight: 700; font-size: 14px;
    color: var(--white); padding-left: 42px; line-height: 28px; letter-spacing: 0.3px;
  }
  .tab--who { top: 34px; background: var(--blue); }
  .tab--features { top: 197px; background: var(--green); }

  .who__text { position: absolute; left: 42px; top: 80px; width: 168px; font-size: 11px; line-height: 13.5px; color: var(--white); }

  .features { position: absolute; left: 42px; top: 244px; width: 300px; list-style: none; color: var(--white); font-size: 9.6px; }
  .features li { position: relative; padding-left: 11px; }
  .features li::before { content: ""; position: absolute; left: 0; top: 4px; width: 5px; height: 5px; border-radius: 50%; background: var(--green); }
  .features > li { margin-bottom: 11.5px; }
  .features ul { list-style: none; margin-top: 13px; margin-bottom: 18px; padding-left: 11px; }
  .features ul li { font-style: italic; font-size: 9.2px; line-height: 11.5px; margin-bottom: 5px; }

  .back__brand { left: 404px; top: 81px; }
  .back__brand .brand__dot { width: 37px; height: 37px; }
  .back__brand .brand__name { font-size: 22px; }
  .stamp { position: absolute; left: 585px; top: 55px; width: 82px; height: 92px; background: var(--stamp); }
  .address-line { position: absolute; left: 411px; width: 241px; height: 1.5px; background: var(--rule); }

  .contact {
    position: absolute; left: 394px; top: 393px;
    font-family: "Montserrat", sans-serif; font-weight: 400; font-size: 15px; line-height: 23.5px;
    color: var(--ink-soft); letter-spacing: 0.3px; font-style: normal;
  }
</style>
</head>
<body>

<section class="postcard postcard--front">
  <svg class="postcard__art" width="699" height="499" viewBox="0 0 699 499">
    <defs>
      <linearGradient id="frontBlue" x1="0" y1="0" x2="0" y2="1">
        <stop offset="0" stop-color="#0a4f8f"/>
        <stop offset="0.6" stop-color="#0d5fa8"/>
        <stop offset="1" stop-color="#0b6cb8"/>
      </linearGradient>
      <linearGradient id="busPhoto" x1="0" y1="0" x2="1" y2="1">
        <stop offset="0" stop-color="#e7a61c"/>
        <stop offset="0.45" stop-color="#6b87b9"/>
        <stop offset="0.75" stop-color="#4f5358"/>
        <stop offset="1" stop-color="#2d2f33"/>
      </linearGradient>
    </defs>
    <path d="M0 290 C40 312 80 330 130 340 C200 352 300 335 366 310 L380 332 C300 362 220 375 150 372 C90 368 40 352 0 338 Z" fill="var(--green)"/>
    <circle cx="520" cy="200" r="200" fill="var(--green)"/>
    <path d="M0 0 H699 V356 C680 366 660 371 640 373 L366 310 C300 335 200 352 130 340 C80 330 40 312 0 290 Z" fill="url(#frontBlue)"/>
    <path d="M640 373 C665 368 685 360 699 350 V372 C685 380 662 387 640 392 Z" fill="#2a8ad8"/>
    <g role="img" aria-label="Photo: children with backpacks boarding a yellow school bus">
      <circle cx="524" cy="194" r="194" fill="url(#busPhoto)" stroke="var(--white)" stroke-width="3"/>
    </g>
    <g class="headline">
      <text x="46" y="64" textLength="266" lengthAdjust="spacingAndGlyphs" font-family="Montserrat, sans-serif" font-weight="300" font-size="36" fill="var(--white)">WE OFFER AN</text>
      <text x="40" y="122" textLength="272" lengthAdjust="spacingAndGlyphs" font-family="'Bebas Neue', sans-serif" font-size="72" fill="var(--green)">AFFORDABLE</text>
      <text x="40" y="169" textLength="272" lengthAdjust="spacingAndGlyphs" font-family="'Bebas Neue', sans-serif" font-size="46" fill="var(--white)">SOFTWARE SOLUTION</text>
      <text x="37" y="230" textLength="276" lengthAdjust="spacingAndGlyphs" font-family="Montserrat, sans-serif" font-weight="900" font-size="61" fill="var(--green)">SCHOOL</text>
      <text x="39" y="282" textLength="274" lengthAdjust="spacingAndGlyphs" font-family="'Bebas Neue', sans-serif" font-size="55" fill="var(--white)">TRANSPORTATION</text>
    </g>
  </svg>

  <div class="brand front__brand">
    <span class="brand__dot"></span>
    <span class="brand__name">VarnoTrak</span>
  </div>
  <div class="front__divider"></div>
  <p class="front__visit">I am visiting ______________ on ______________ and would like to stop by your office to introduce myself and show you how our platform serves your district.</p>
</section>

<section class="postcard postcard--back">
  <svg class="postcard__art" width="699" height="499" viewBox="0 0 699 499">
    <defs>
      <linearGradient id="backBlue" x1="0" y1="0" x2="0" y2="1">
        <stop offset="0" stop-color="#0b6cb8"/>
        <stop offset="0.7" stop-color="#0a64ad"/>
        <stop offset="1" stop-color="#0a4f8f"/>
      </linearGradient>
      <linearGradient id="phonePhoto" x1="0" y1="0" x2="1" y2="1">
        <stop offset="0" stop-color="#e9e6e4"/>
        <stop offset="0.45" stop-color="#d9b0a6"/>
        <stop offset="0.7" stop-color="#2b2b2e"/>
        <stop offset="1" stop-color="#cfc9c6"/>
      </linearGradient>
    </defs>
    <rect x="300" y="380" width="341" height="98" rx="49" fill="var(--green)"/>
    <path d="M0 140 H330 C385 160 395 260 372 340 C360 400 345 450 325 499 H0 Z" fill="url(#backBlue)"/>
    <path d="M0 0 H400 C350 40 305 85 270 118 C200 165 100 172 0 163 Z" fill="var(--green)"/>
    <g role="img" aria-label="Photo: hand holding a smartphone showing a route map">
      <circle cx="300" cy="160" r="93" fill="url(#phonePhoto)" stroke="var(--white)" stroke-width="3"/>
    </g>
  </svg>

  <div class="tab tab--who">WHO WE ARE:</div>
  <p class="who__text">VarnoTrak provides a solution for school transportation that integrates all features into a single, cloud based technology.</p>

  <div class="tab tab--features">FEATURES</div>
  <ul class="features">
    <li>Student Tracking
      <ul>
        <li>Who, When and Where your buses were boarded<br>and alighted</li>
        <li>Live cloud reporting to find lost students</li>
        <li>Load factor reporting to monitor efficiency.</li>
      </ul>
    </li>
    <li>Turn-by-turn directions to keep drivers updated and informed</li>
    <li>Route Optimization saving more than 10% on transportation cost*</li>
    <li>Field Trip workflow to automate the athletic and field trips</li>
    <li>Parent App to share bus information with your school community</li>
    <li>Complete GPS Support</li>
  </ul>

  <div class="brand back__brand">
    <span class="brand__dot"></span>
    <span class="brand__name">VarnoTrak</span>
  </div>
  <div class="stamp"></div>
  <div class="address-line" style="top:231px"></div>
  <div class="address-line" style="top:268px"></div>
  <div class="address-line" style="top:310px"></div>

  <address class="contact">
    VarnoTrak LLC<br>
    Bayford ME | Carlsmont, CA<br>
    Office (207) 555-0148
  </address>
</section>

</body>
</html>
```